Futuristic and Visually Appealing Photo Booth Rental Website

I need a Photo Booth rental website made for easy editing through Wordpress. Web design + Page Templates are needed for showcasing booths, packages, experiences, and add-ons. There's a space and futuristic theme to the company that I'd like to stick with. I'd like to integrate certain parts of the site with html code (iframe) but others with text, pictures, and video. I'd like the design as complete as possible while I help work on the content as much as I can. The priority should be making the site friendly enough to educate and convert sales/bookings. I have no problem working from a general photobooth website as a base.

Company: SnapTrek NX

Coding required. All source files needed to install as theme that can be edited by something like Elementor.

**Contact for current design done under maintenance mode**

Target Market(s)

All consumers (holiday parties, birthdays, weddings, etc...)
Corporate Clients (conventions, virtual expos, holiday parties, company events)

Industry/Entity Type

Events

Coding

Coded - Design and coding required

Font styles to use
Sans Serif

Requirements
Must have
• ===Menu/Submenu===
Our Booths: DSLR Open Air Photo Booth, Selfie Station, Drifta, Pendulum Skiv, LumaVex
Consumers: Rental Packages, Addons
Corporate: Experiences, Addons, Build-to-Suit, Get a Quote (iframe)
About: About Us, Non-Profits, Employment
Customizations: Printout Templates (iframe), Start Screens (iframe), Backdrops
Contact Us: Inquiry, Custom Quote

===Buttons/Call to Action===
Book Online
Find My Photos
Client Portal

Social Media Icons and Footer section for vendor buttons (vowlinker, quib, the plume, etc...)

Responsive design
Nice to have
• Video Slides on Frontpage
Should not have
• OnePage Design

```html
<!DOCTYPE html>
<html lang="en">
<head>
<meta charset="utf-8">
<title>SnapTrek NX — Futuristic Photo Booth Rental</title>
<link rel="stylesheet" href="https://fonts.googleapis.com/css2?family=Lato:wght@300;400;700;900&family=Allura&display=swap">
<style>
:root{
  --night:#0f2729;
  --hero:#1f4b4b;
  --ink:#1f4648;
  --gold:#e8b73c;
  --teal:#2bc4c0;
  --mist:#f4f6f5;
  --aqua:#c8e8e6;
  --footer:#122628;
  --text:#3c4a4b;
  --dot:#3a4b4c;
}
*{margin:0;padding:0;box-sizing:border-box}
html,body{width:1200px;height:3223px;overflow:hidden}
body{position:relative;background:#fff;font-family:'Lato',sans-serif;color:var(--text)}
.abs{position:absolute}
.script{font-family:'Allura',cursive}

/* header / hero */
.top-band{left:0;top:0;width:1200px;height:696px;background:var(--night)}
.below-hero{left:0;top:696px;width:1200px;height:700px;background:var(--mist)}
.ghost-word{font-weight:900;color:rgba(255,255,255,.05);line-height:1;letter-spacing:2px}
.logo{left:60px;top:22px;display:flex;align-items:center;gap:10px}
.logo-dot{width:48px;height:48px;border-radius:50%;background:var(--teal)}
.logo-name{font-weight:900;font-size:16px;color:#fff}
.nav{top:57px;display:flex;font-size:13px;color:#c9d3d3;text-transform:uppercase}
.nav span{position:absolute;white-space:nowrap}
.nav .active{color:#fff;font-weight:700}
.nav-bar{left:275px;top:84px;width:48px;height:4px;background:var(--teal);border-radius:2px}
.side-dot{width:44px;height:44px;border-radius:50%;background:var(--dot);left:27px}
.hero-card{left:100px;top:206px;width:1100px;height:522px;background:var(--hero);border-top-left-radius:26px}
.hero-title{left:185px;top:296px;font-size:40px;font-weight:300;color:var(--gold);line-height:58px}
.hero-copy{left:187px;top:434px;width:330px;font-size:16px;line-height:32px;color:#fff}
.btn{display:flex;align-items:center;justify-content:center;background:var(--gold);border-radius:22px;font-weight:900;letter-spacing:1.5px;color:var(--ink);font-size:15px}
.hero-btn{left:185px;top:588px;width:155px;height:44px}
.booth{left:644px;top:138px;width:313px;height:590px;background:linear-gradient(180deg,#f2f3f3,#d8dcdc);border-radius:30px 30px 0 0}
.slide-no{left:1026px;top:500px;font-size:78px;font-weight:700;color:var(--gold)}
.slide-of{left:1072px;top:513px;font-size:26px;font-weight:300;color:#c9d3d3}
.arrow{width:52px;height:52px;border-radius:50%}
.scroll{left:575px;top:703px;width:50px;height:50px;border-radius:50%;background:#fff;box-shadow:0 4px 12px rgba(0,0,0,.12)}

/* find photos */
.find-1{left:105px;top:838px;font-size:56px;font-weight:300;color:var(--ink)}
.find-2{left:105px;top:910px;font-size:60px;font-weight:700;color:var(--ink)}
.search{left:417px;top:928px;width:683px;height:40px;border-bottom:2px solid #c9d0d0}
.search-ph{left:28px;top:10px;font-size:16px;color:#b3b9b9}
.card{top:1033px;width:223px;height:278px;background:#fff;box-shadow:0 4px 14px rgba(0,0,0,.07)}
.card-img{position:absolute;left:10px;top:10px;width:203px;height:186px}
.card-name{position:absolute;left:0;top:210px;width:100%;text-align:center;font-size:40px;color:var(--gold)}

/* portal */
.ghost-gray{font-weight:900;color:rgba(0,0,0,.035);line-height:1}
.section-title{font-size:35px;font-weight:300;color:var(--ink)}
.section-title b{color:var(--gold);font-weight:700}
.tile{width:223px;height:183px;border-radius:4px}
.tile-cap{width:223px;text-align:center;font-size:19px;color:var(--ink)}

/* vendors */
.vendor{font-size:30px;color:#555;display:flex;align-items:center;gap:8px;white-space:nowrap}
.vendor i{display:block;width:26px;height:26px;background:#777;border-radius:50%}

/* contact */
.contact-bg{left:0;top:2411px;width:1200px;height:680px}
.quote-card{left:100px;top:2671px;width:404px;height:132px;background:#fff;box-shadow:0 6px 16px rgba(0,0,0,.06)}
.quote-text{left:30px;top:40px;width:350px;font-size:12px;line-height:21px;color:#444}
.field{background:#fff;border-radius:21px;font-size:9.5px;letter-spacing:.5px;color:#8a9393;padding:15px 0 0 20px;text-transform:uppercase}
.footer{left:0;top:3090px;width:1200px;height:133px;background:var(--footer);color:#fff;font-size:12.5px}
</style>
</head>
<body>

<!-- hero -->
<div class="abs top-band"></div>
<div class="abs below-hero"></div>
<div class="abs ghost-word" style="left:38px;top:118px;font-size:142px">BOOTH</div>
<div class="abs ghost-word" style="left:38px;top:295px;font-size:142px">M</div>

<div class="abs logo"><span class="logo-dot"></span><span class="logo-name">SnapTrek NX</span></div>
<nav class="abs nav" style="left:0;width:1200px">
  <span class="active" style="left:300px">Home</span>
  <span style="left:393px">Our Booth</span>
  <span style="left:517px">Consumer</span>
  <span style="left:636px">Corporate</span>
  <span style="left:764px">About</span>
  <span style="left:857px">Customizations</span>
  <span style="left:1025px">Contact Us</span>
</nav>
<div class="abs nav-bar"></div>

<div class="abs side-dot" style="top:427px"></div>
<div class="abs side-dot" style="top:488px"></div>
<div class="abs side-dot" style="top:548px"></div>
<div class="abs side-dot" style="top:610px"></div>

<div class="abs hero-card"></div>
<h1 class="abs hero-title">Futuristic and Visually<br>Appealing Photo Booth</h1>
<p class="abs hero-copy">Lorem ipsum dolor sit amet, consectetur adipiscing elit. Integer eleifend nisi erat, sed luctus orci consectetur ut.</p>
<a class="abs btn hero-btn">BOOK NOW!</a>
<div class="abs booth" role="img" aria-label="White kiosk photo booth with camera, screen and printer on a stand"></div>
<div class="abs slide-no">1</div>
<div class="abs slide-of">/3</div>
<div class="abs arrow" style="left:1021px;top:611px;background:rgba(255,255,255,.06)">
  <svg width="52" height="52"><path d="M29 20l-6 6 6 6" stroke="#5f7878" stroke-width="2" fill="none"/></svg>
</div>
<div class="abs arrow" style="left:1086px;top:611px;background:#15393a">
  <svg width="52" height="52"><path d="M23 20l6 6-6 6" stroke="#fff" stroke-width="2" fill="none"/></svg>
</div>
<div class="abs scroll">
  <svg width="50" height="50"><rect x="19" y="14" width="12" height="21" rx="6" stroke="#e8b73c" stroke-width="2" fill="none"/><line x1="25" y1="18" x2="25" y2="23" stroke="#e8b73c" stroke-width="2"/></svg>
</div>

<!-- find my photos -->
<h2 class="abs find-1">Find</h2>
<h2 class="abs find-2">My Photos</h2>
<div class="abs search">
  <span class="abs search-ph">Search your photos</span>
  <svg class="abs" style="right:16px;top:6px" width="24" height="24"><circle cx="10" cy="10" r="7" stroke="#e8b73c" stroke-width="2.5" fill="none"/><line x1="15" y1="15" x2="21" y2="21" stroke="#e8b73c" stroke-width="2.5"/></svg>
</div>

<div class="abs card" style="left:119px"><div class="card-img" role="img" aria-label="Two decorated wedding chairs on a lawn" style="background:linear-gradient(180deg,#a9c7a0,#6e9a4c)"></div><div class="card-name script">Tamsin Photos</div></div>
<div class="abs card" style="left:378px"><div class="card-img" role="img" aria-label="Wedding couple beside a vintage van" style="background:linear-gradient(180deg,#c9ccc8,#7b7f7d)"></div><div class="card-name script">Aquillarius</div></div>
<div class="abs card" style="left:637px"><div class="card-img" role="img" aria-label="White rose among dark leaves" style="background:radial-gradient(circle at 55% 45%,#f4f1e6 0,#e6e2cf 30%,#1e3e33 60%)"></div><div class="card-name script">Selma Rowe</div></div>
<div class="abs card" style="left:895px"><div class="card-img" role="img" aria-label="Portrait in front of pink flowers" style="background:linear-gradient(180deg,#d98b97,#8f5b4c)"></div><div class="card-name script">Wonderfull</div></div>
<div class="abs card" style="left:1152px"><div class="card-img" role="img" aria-label="Portrait with flower crown" style="background:linear-gradient(180deg,#c9a46e,#b45a3e)"></div></div>
<div class="abs arrow" style="left:1086px;top:1139px;background:#fff;box-shadow:0 3px 10px rgba(0,0,0,.12)">
  <svg width="52" height="52"><path d="M23 20l6 6-6 6" stroke="#1f4648" stroke-width="2" fill="none"/></svg>
</div>

<!-- client portal -->
<svg class="abs" style="left:0;top:1355px" width="1200" height="185"><polygon points="0,5 1200,178 1200,185 0,185" fill="#fff"/></svg>
<div class="abs ghost-gray" style="left:15px;top:1415px;font-size:140px">CLIENT</div>
<div class="abs ghost-gray" style="left:713px;top:1715px;font-size:140px">PORTA</div>
<h2 class="abs section-title" style="left:98px;top:1462px">Client <b>Portal</b></h2>

<div class="abs tile" style="left:100px;top:1534px;background:linear-gradient(160deg,#7fa3bb,#24374a)" role="img" aria-label="Hand holding a camera in blue haze"></div>
<div class="abs tile" style="left:358px;top:1534px;background:linear-gradient(160deg,#3a3b3c,#b9b9b3)" role="img" aria-label="Camera photographing a stack of macarons"></div>
<div class="abs tile" style="left:617px;top:1534px;background:linear-gradient(160deg,#e3d9d2,#c4587a)" role="img" aria-label="Toddler with a toy camera"></div>
<div class="abs tile" style="left:874px;top:1534px;background:linear-gradient(160deg,#8fd0d6,#b48b3a)" role="img" aria-label="Pineapple on a pale blue background"></div>
<div class="abs tile-cap" style="left:100px;top:1725px">7 Photography Trick</div>
<div class="abs tile-cap" style="left:358px;top:1725px">Food Photography</div>
<div class="abs tile-cap" style="left:617px;top:1725px">How to Photography</div>
<div class="abs tile-cap" style="left:874px;top:1725px">Fruits Mentariana</div>

<div class="abs tile" style="left:100px;top:1798px;background:linear-gradient(160deg,#2c2620,#c9b19a)" role="img" aria-label="Chef plating food on a board"></div>
<div class="abs tile" style="left:358px;top:1798px;background:linear-gradient(160deg,#9c6e4c,#d85b34)" role="img" aria-label="Phone photographing a breakfast dish"></div>
<div class="abs tile" style="left:617px;top:1798px;background:linear-gradient(160deg,#e04a1d,#f6a64a)" role="img" aria-label="Halved papaya"></div>
<div class="abs tile" style="left:874px;top:1798px;background:linear-gradient(160deg,#4f5a44,#c7b6a6)" role="img" aria-label="Person photographing a meal at a table"></div>
<div class="abs tile-cap" style="left:100px;top:1989px">3 Trick for food</div>
<div class="abs tile-cap" style="left:358px;top:1989px">Phone 3 Trick</div>
<div class="abs tile-cap" style="left:617px;top:1989px">7 Photography Trick</div>
<div class="abs tile-cap" style="left:874px;top:1989px">7 Photography Trick</div>

<!-- vendors -->
<h2 class="abs section-title" style="left:0;width:1192px;text-align:center;top:2106px">Our <b>Vendor</b></h2>
<div class="abs vendor" style="left:285px;top:2218px;font-size:21px;letter-spacing:1px"><i style="width:24px;height:24px;background:none;border:1.5px solid #777"></i>VOWLINKER</div>
<div class="abs vendor" style="left:548px;top:2212px;font-size:34px;color:#aaa;font-weight:300">the plume</div>
<div class="abs vendor" style="left:765px;top:2210px;font-size:36px;color:#111;font-weight:900">quib</div>
<div class="abs vendor" style="left:178px;top:2314px;font-size:29px;color:#333"><i style="border-radius:4px;width:48px;height:40px;background:#777"></i>Parcelo</div>
<div class="abs vendor" style="left:418px;top:2316px;font-size:30px;color:#111">Atelier</div>
<div class="abs vendor" style="left:612px;top:2313px;font-size:36px;color:#222;font-weight:700"><i style="width:46px;height:46px;background:#666"></i>Nestwing</div>
<div class="abs vendor" style="left:888px;top:2310px;font-size:37px;color:#555">Voyamo</div>

<!-- contact -->
<svg class="abs contact-bg" width="1200" height="680"><polygon points="0,60 1200,0 1200,680 0,680" fill="#c8e8e6"/></svg>
<h2 class="abs" style="left:106px;top:2590px;font-size:33px;font-weight:300;color:var(--ink)">What our <b style="font-weight:700">clients say</b></h2>
<div class="abs quote-card"><p class="abs quote-text">Sed ut perspiciatis unde omnis iste natus error sit voluptatem accusantium doloremque laudantium, totam rem aperiam, eaque ipsa quae ab illo inventore veritatis et quasi architecto.</p></div>
<svg class="abs" style="left:420px;top:2802px" width="30" height="18"><polygon points="0,0 28,0 2,16" fill="#fff"/></svg>
<div class="abs" style="left:130px;top:2653px;width:38px;height:38px;border-radius:50%;background:var(--ink);color:#fff;font-size:26px;font-weight:900;text-align:center;line-height:46px">“</div>
<div class="abs" style="left:200px;top:2843px;width:176px;text-align:right;font-size:15px;color:var(--ink)">MIRA SOLEN</div>
<div class="abs" style="left:200px;top:2869px;width:176px;text-align:right;font-size:9px;color:#555">EO CEO</div>
<div class="abs" role="img" aria-label="Client portrait" style="left:387px;top:2832px;width:66px;height:66px;border-radius:50%;background:linear-gradient(160deg,#8a8f92,#2f3436)"></div>

<h2 class="abs" style="left:600px;top:2532px;font-size:35px;font-weight:700;color:var(--ink)">Contact <span style="font-weight:300">us</span></h2>
<p class="abs" style="left:600px;top:2582px;font-size:12.5px;color:#333">Do you have questions? Complete the form below and we'll get back to you asap</p>
<div class="abs field" style="left:600px;top:2632px;width:229px;height:41px">Your Name *</div>
<div class="abs field" style="left:857px;top:2632px;width:230px;height:41px">Email Address *</div>
<div class="abs field" style="left:600px;top:2699px;width:229px;height:41px">Phone Number</div>
<div class="abs field" style="left:857px;top:2699px;width:230px;height:41px">Subject</div>
<div class="abs field" style="left:600px;top:2765px;width:487px;height:125px">Your Message</div>
<a class="abs btn" style="left:600px;top:2930px;width:154px;height:44px">SUBMIT</a>

<!-- footer -->
<footer class="abs footer">
  <div class="abs" style="left:100px;top:44px">Terms of Service &amp; Refund Policy &nbsp;/&nbsp; Privacy Policy</div>
  <div class="abs" style="left:100px;top:77px">© 2020 SnapTrek NX, LLC</div>
  <div class="abs" style="right:100px;top:34px;text-align:right;line-height:20px">4120 Orbit Lane, Halden, TX 75010<br>Business Hours: M-F 8-5pm CST<br>(012) 555-0147</div>
</footer>

</body>
</html>
```